Copper Kettle Catering
Business Cards and Letterhead
Copper Kettle Catering -
Creative Brief
Use standard fonts
R Danela Forsythe
Chef/Owner
287 W 93rd St FL2 New York, NY 10025
copperkettlecatering@mailbox.example
copperkettlecatering.example

```html
<!DOCTYPE html>
<html lang="en">
<head>
<meta charset="utf-8">
<title>Copper Kettle Catering – Business Card</title>
<link href="https://fonts.googleapis.com/css2?family=Arimo:wght@400;700&display=swap" rel="stylesheet">
<style>
  :root{
    --backdrop:#6e4d31;
    --card:#ffffff;
    --ink:#3a3a3a;
    --ink-soft:#555555;
    --brand-red:#c41f28;
    --brand-red-dark:#8f1118;
    --silver-light:#e6e6e6;
    --silver-dark:#9a9a9a;
  }
  *{box-sizing:border-box;margin:0;padding:0}
  html,body{width:1200px;height:367px;overflow:hidden}
  body{background:var(--backdrop);font-family:"Arimo",Arial,sans-serif;color:var(--ink);position:relative}
  .card{position:absolute;top:24px;width:564px;height:314px;background:var(--card);border-radius:22px;overflow:hidden;box-shadow:0 2px 6px rgba(0,0,0,.35)}
  .card--front{left:24px}
  .card--back{left:612px}

  .brand-name{color:var(--brand-red);font-weight:700;line-height:1.05}
  .card--front .brand-name{position:absolute;left:36px;top:112px;width:250px;font-size:30px}
  .card--back .brand-name{position:absolute;left:0;right:0;top:110px;text-align:center;font-size:44px}

  .person{position:absolute;left:300px;top:22px}
  .person__name{font-size:17px;color:var(--ink)}
  .person__role{font-size:11.5px;color:var(--ink-soft);margin-top:8px}

  .contact{position:absolute;left:300px;top:112px;font-size:11.5px;line-height:18px;color:var(--ink);white-space:nowrap}
  .contact__address{margin-bottom:12px}
  .contact__lines{line-height:20px}

  .swoosh{position:absolute;left:0;bottom:0;width:564px;height:100px}
  .card--front .website{position:absolute;right:36px;bottom:14px;font-size:12px;color:#fff}
  .card--back .website{position:absolute;left:0;right:0;bottom:34px;text-align:center;font-size:12.5px;color:var(--ink)}
</style>
</head>
<body>
  <section class="card card--front">
    <div class="brand-name">Copper Kettle Catering</div>

    <div class="person">
      <p class="person__name">R Danela Forsythe</p>
      <p class="person__role">Chef/Owner</p>
    </div>

    <div class="contact">
      <p class="contact__address">287 W 93rd St FL2<br>New York, NY 10025</p>
      <p class="contact__lines">P : 212.555.0148<br>F : 212.555.0193<br>E : copperkettlecatering@mailbox.example</p>
    </div>

    <svg class="swoosh" viewBox="0 0 564 100" aria-hidden="true">
      <defs>
        <linearGradient id="silverBand" x1="0" y1="0" x2="1" y2="0">
          <stop offset="0" stop-color="var(--silver-light)"/>
          <stop offset="0.6" stop-color="var(--silver-dark)"/>
          <stop offset="1" stop-color="var(--silver-light)"/>
        </linearGradient>
        <linearGradient id="redBand" x1="0" y1="0" x2="1" y2="0">
          <stop offset="0" stop-color="var(--brand-red-dark)"/>
          <stop offset="0.5" stop-color="var(--brand-red)"/>
          <stop offset="1" stop-color="var(--brand-red-dark)"/>
        </linearGradient>
      </defs>
      <path d="M0 28 C150 82 330 66 564 24 L564 56 C360 92 160 100 0 58 Z" fill="url(#silverBand)"/>
      <path d="M0 52 C170 96 360 84 564 44 L564 100 L0 100 Z" fill="url(#redBand)"/>
    </svg>
    <p class="website">www.copperkettlecatering.example</p>
  </section>

  <section class="card card--back">
    <div class="brand-name">Copper Kettle<br>Catering</div>
    <p class="website">www.copperkettlecatering.example</p>
  </section>
</body>
</html>
```